Harrow Spirits Bottle Label

BACKGROUND
We are plumbers that have resurrected London's oldest once illicit Gin Distillery KTV Report https://www.vidstream-example.com/watch?v=Qx8rTmL2pWa&t=4s
Bought 150yr old derelict bakery & turned it into an office for our plumbing biz....removed dangerous chimney...got sued by a neighbour ..
our lawyers discovered that the original bakers family once made illict gin here (in what is now our office) we tracked down the origianl family ...see pic enclosed....the little boy now in his 90's (Colin Fenwort) gave us his family's secret gin recipe and we have now resurrected it. We supply Aldermoor Hall, Hse of Elders Pettigrew Hale etc. Now have our 1st Harrow Spirits.
This is NOT scotch whisky...this a brand new category of drink 'English Whisky'
1. traditional whisky style bottle which will have embossed text on as per the sample English Whisky & K T Distillery LONDON
Front label 110mm x 95mm
Rear label 70mm wide and 100mm
Front Text Harrow Spirits
Rear Text Harrow Spirits
Must have a old map of my area London Q27 8XZ on rear
Map link https://charts.oldplans-example.org/view-full/558201736#zoom=6&lat=1477&lon=6570&layers=BT

Target Market(s)

OVER 30's

Font styles to use
Sans Serif

Requirements
Nice to have
• I want an old map on the front of the label....the map have 2 small rivers on it which are very close to my distillery (called The Calder Race and Tollet Beck, where they meet there a small bridge called Harecroft Bridge, i would like this shown on the map, is there any tasteful way to add some colour to the historic map ???

```html
<!DOCTYPE html>
<html lang="en">
<head>
<meta charset="utf-8">
<title>Harrow Spirits – English Whisky Labels</title>
<link rel="stylesheet" href="https://fonts.googleapis.com/css2?family=Oswald:wght@500;600&family=Libre+Baskerville&display=swap">
<style>
  :root {
    --paper: #ffffff;
    --label-black: #232323;
    --silver: #c9c9c9;
    --silver-light: #e8e8e8;
    --silver-dim: #8f8f8f;
    --copy: #bdbdbd;
    --map-light: #ece8d6;
    --map-dark: #d8d2b8;
  }
  * { box-sizing: border-box; margin: 0; padding: 0; }
  html, body {
    width: 1200px; height: 1200px; overflow: hidden;
    background: var(--paper);
  }
  .canvas { position: relative; width: 1200px; height: 1200px; }

  .label { position: absolute; }
  .label-frame { position: absolute; inset: 0; }

  .brand-name {
    font-family: "Oswald", sans-serif; font-weight: 500;
    color: var(--silver-light); text-transform: uppercase;
    line-height: 1; white-space: nowrap; text-align: center;
  }

  /* Front label */
  .front-label { left: 110px; top: 360px; width: 520px; height: 449px; }
  .brand-box {
    position: absolute; left: 82px; top: 100px; width: 356px; height: 150px;
    display: flex; align-items: center; justify-content: center;
    padding: 0 20px;
  }
  .front-label .brand-name { font-size: 44px; letter-spacing: 3px; }
  .category {
    position: absolute; left: 0; right: 0; top: 268px; text-align: center;
    font-family: "Oswald", sans-serif; font-weight: 600; font-size: 46px;
    letter-spacing: 1px; color: var(--silver-light); line-height: 1;
    white-space: nowrap;
  }
  .distillery {
    position: absolute; left: 0; right: 0; top: 334px; text-align: center;
    font-family: "Libre Baskerville", serif; font-size: 13px;
    letter-spacing: 4px; color: var(--silver-dim); white-space: nowrap;
  }

  /* Rear label */
  .rear-label { left: 720px; top: 335px; width: 370px; height: 520px; }
  .rear-label .brand-name {
    position: absolute; left: 0; right: 0; top: 36px;
    font-size: 30px; letter-spacing: 2px;
  }
  .rear-intro, .rear-notes, .volume {
    position: absolute; left: 0; right: 0; text-align: center;
    font-family: "Libre Baskerville", serif; color: var(--copy);
  }
  .rear-intro { top: 100px; padding: 0 16px; font-size: 9px; line-height: 14px; }
  .map-area {
    position: absolute; left: 22px; top: 168px; width: 326px; height: 224px;
    background: linear-gradient(135deg, var(--map-light), var(--map-dark));
  }
  .volume { top: 410px; font-size: 8px; color: var(--silver-dim); }
  .rear-notes { top: 424px; padding: 0 105px; font-size: 9px; line-height: 14px; }
</style>
</head>
<body>
<main class="canvas">

  <section class="label front-label" aria-label="Front label">
    <svg class="label-frame" width="520" height="449" viewBox="0 0 520 449">
      <rect width="520" height="449" fill="var(--label-black)"/>
      <g fill="none" stroke="var(--silver)">
        <line x1="22" y1="24" x2="498" y2="24" stroke-width="3"/>
        <line x1="22" y1="425" x2="498" y2="425" stroke-width="3"/>
        <path d="M22,40 A10,10 0 0 1 12,50 V399 A10,10 0 0 1 22,409" stroke-width="1.5"/>
        <path d="M498,40 A10,10 0 0 0 508,50 V399 A10,10 0 0 0 498,409" stroke-width="1.5"/>
        <path d="M90,100 H430 A8,8 0 0 0 438,108 V242 A8,8 0 0 0 430,250 H90 A8,8 0 0 0 82,242 V108 A8,8 0 0 0 90,100 Z" stroke-width="1.2"/>
      </g>
      <g stroke="var(--silver-dim)" stroke-width="1.5">
        <line x1="40" y1="42" x2="100" y2="42" stroke-dasharray="3 3"/>
        <line x1="420" y1="42" x2="480" y2="42" stroke-dasharray="3 3"/>
        <line x1="40" y1="406" x2="100" y2="406" stroke-dasharray="3 3"/>
        <line x1="420" y1="406" x2="480" y2="406" stroke-dasharray="3 3"/>
      </g>
    </svg>
    <div class="brand-box"><span class="brand-name">Harrow Spirits</span></div>
    <p class="category">ENGLISH WHISKY</p>
    <p class="distillery">KT DISTILLERY LONDON</p>
  </section>

  <section class="label rear-label" aria-label="Rear label">
    <svg class="label-frame" width="370" height="520" viewBox="0 0 370 520">
      <path d="M22,3 H348 A19,19 0 0 0 367,22 V498 A19,19 0 0 0 348,517 H22 A19,19 0 0 0 3,498 V22 A19,19 0 0 0 22,3 Z"
            fill="var(--label-black)" stroke="var(--silver)" stroke-width="3"/>
    </svg>
    <p class="brand-name">Harrow Spirits</p>
    <p class="rear-intro">Lorem ipsum dolor sit amet, consectetuer adipiscing elit, sed diam nonummy nibh euismod tincidunt ut laoreet dolore magna aliquam erat volutpat. Ut wisi enim ad minim veniam, quis</p>
    <div class="map-area" role="img" aria-label="Historic survey map of the distillery area around Q27 8XZ, showing The Calder Race, Tollet Beck and Harecroft Bridge"></div>
    <p class="volume">500ML</p>
    <p class="rear-notes">Lorem ipsum dolor sit amet, consectetuer adipiscing elit, sed diam nonummy nibh euismod</p>
  </section>

</main>
</body>
</html>
```